Social Media Graphics - ALL TEXT RK

We are looking for a series of social media graphics for Instagram (standard size 1:1 (1080x1080px) that are ALL TEXT. We want the following quotes below on each graphic; one quote per graphic. AND, In very small letters at the bottom of each graphic, add @RKMarlowLive

The look and feel of these graphics should be complimentary to the color palette attached below; but keep them simple. But the design is up to you; at the end of this document, I provided various samples of all text graphics that I like as examples.

Target Market(s)

women looking to lose weight

Industry/Entity Type

health and wellness

Colors
E54698
E96AAD
F1A4CE
F9D9EA
FCEFF6

Requirements
Must have
• the quotes in the document
Should not have
• no stock photography

```html
<!DOCTYPE html>
<html lang="en">
<head>
<meta charset="utf-8">
<title>Bloating Quote Graphic</title>
<link href="https://fonts.googleapis.com/css2?family=Montserrat:wght@400;900&display=swap" rel="stylesheet">
<style>
  :root {
    --magenta-deep: #d01a68;
    --magenta-mid: #dc3f80;
    --pink-glow: #ee6aa8;
    --bubble-soft: rgba(249, 217, 234, 0.12);
    --bubble-strong: rgba(241, 164, 206, 0.22);
    --ring-line: rgba(252, 239, 246, 0.45);
    --plus-mark: rgba(252, 239, 246, 0.7);
    --text-white: #ffffff;
    --handle-tint: #f9d9ea;
  }
  html, body { margin: 0; padding: 0; overflow: hidden; }
  .canvas {
    position: relative;
    width: 1200px;
    height: 1200px;
    overflow: hidden;
    background: radial-gradient(circle at 46% 47%, var(--pink-glow) 0%, var(--magenta-mid) 38%, var(--magenta-deep) 72%);
    font-family: "Montserrat", sans-serif;
  }
  .decor { position: absolute; inset: 0; width: 1200px; height: 1200px; }
  .quote {
    position: absolute;
    left: 222px;
    top: 262px;
    margin: 0;
    color: var(--text-white);
    font-size: 89px;
    line-height: 97px;
    font-weight: 400;
    letter-spacing: 1px;
  }
  .quote strong { font-weight: 900; font-size: 90px; letter-spacing: 0.5px; }
  .handle {
    position: absolute;
    left: 204px;
    top: 1092px;
    color: var(--handle-tint);
    font-size: 34px;
    font-weight: 400;
  }
</style>
</head>
<body>
<div class="canvas">
  <svg class="decor" viewBox="0 0 1200 1200" aria-hidden="true">
    <g class="bubbles">
      <circle cx="1080" cy="120" r="190" fill="var(--bubble-soft)"/>
      <circle cx="1010" cy="230" r="70" fill="var(--bubble-strong)"/>
      <circle cx="60" cy="1130" r="210" fill="var(--bubble-soft)"/>
      <circle cx="170" cy="1000" r="44" fill="var(--bubble-strong)"/>
      <circle cx="90" cy="120" r="120" fill="var(--bubble-soft)"/>
      <circle cx="1130" cy="1060" r="95" fill="var(--bubble-strong)"/>
    </g>
    <g class="rings" fill="none" stroke="var(--ring-line)" stroke-width="2">
      <circle cx="1080" cy="120" r="235"/>
      <circle cx="60" cy="1130" r="255"/>
      <circle cx="1090" cy="640" r="36"/>
    </g>
    <g class="plus-marks" stroke="var(--plus-mark)" stroke-width="4" stroke-linecap="round">
      <path d="M100 470v30M85 485h30"/>
      <path d="M1110 480v24M1098 492h24"/>
      <path d="M960 1010v24M948 1022h24"/>
      <path d="M620 120v24M608 132h24"/>
    </g>
  </svg>

  <p class="quote"><strong>Struggling</strong><br>with bloating<br>and <strong>belly fat?</strong><br>Try this natural<br>solution tonight,<br>and wake up<br><strong>feeling lighter!</strong></p>

  <div class="handle">@RKMarlowLive</div>
</div>
</body>
</html>
```